Commercial Web Site for software product

Ledgerly is a GDPR compliant Membership, Contact Management & List Management solution. It is an ideal replacement for any organisation or company still using Gridsheet, Mailroom, simple database or paper-based system to manage contact data, mail lists, and other personal information.
The target market will be Clubs/Associations in the EU.
The design will need to be a fluid design and suitable for mobile devices. The home page will contain most of the web site content, enabling a user to scroll through all the relevant information on one page. There will be a single sub page design required for supporting information.
The web site will need to support two language versions - English and German (Language selection option required). However, the build requirements will be for a static HTML site (no database) in English only. We will duplicate and make the German version ourselves.
The attached document is the first draft of the home page content. Whilst it is a little wordy, it should convey the main information that we wish to get across.
Please note: We would prefer not to use photographs for the main imagery, we feel vector graphics would be a better option . As a guide, the following design: https://en.pixelvane.example/profiles/Marlowe/designs/5502147 may provide an insight into how we imagine the home page working and contains all the key elements we would expect to be covered.
The logo contained in the attached document can be split into a logo and text. Feel free to use only the logo (without text) or separate and place the text alongside etc., We do not want to change the logo, however, how you chose to use it is up to you.
Colour's are also optional. We like the blue, but are open to alternative ideas.
The testimonials section, should contain all the questions (3) and several of the associated answers shown. Questions/Answers may be separated into speech bubbles or similar. Not all answers will be used, but are there to provide some content.
The sub pages will be used to provide background on the GDPR requirements, our Service Offering, About Us (possibly), and a contact page.
Updates
The design budget is now guaranteed.
Whilst we have no intention not to move forward with this project, I understand the 'lack of commitment' from our side may be a negative.
Once we have reviewed all submissions - we will decide upon our preferred submission.
We will only request changes from one or two designers, and will make it clear how many other designers are in the running. This I believe is fair, as you probably need this information before deciding whether to submit any changes requested!
My hope is we have a home page that enables a visitor to clearly understand what we are offering, without having to drill down into various sub pages or sections to understand the basics. I appreciate we need to write appropriate content, but the design itself should feel uncluttered and fluid.
Hopefully some of you really talented designers can throw some ideas into the pot. The concept is more important than the detail.
Thanks for considering this project.
Coding
Number of Pages Required
Font styles to use
Colors
Look and feel

```html
<!DOCTYPE html>
<html lang="en">
<head>
<meta charset="utf-8">
<title>Ledgerly – Membership &amp; Contact Management Made Simple</title>
<link rel="stylesheet" href="https://fonts.googleapis.com/css2?family=Rubik:wght@500;600;700&family=Roboto:wght@400;500;700&display=swap">
<style>
:root{
  --blue:#0d4fd6;
  --blue-deep:#0a55d9;
  --hero-a:#41a7ec;
  --hero-b:#3c55d3;
  --ink:#111521;
  --text:#4a4f5c;
  --muted:#8a8f9c;
  --tint:#eef4fd;
  --line:#c9ced8;
  --white:#ffffff;
  --star:#f7b500;
  --card-shadow:0 6px 22px rgba(40,70,140,.10);
}
*{box-sizing:border-box;margin:0;padding:0}
html,body{width:1200px;height:4132px;overflow:hidden}
body{font-family:'Roboto',Arial,sans-serif;color:var(--text);background:var(--white);position:relative}
h1,h2,h3,.brand-name{font-family:'Rubik',Arial,sans-serif;color:var(--ink)}
section,footer{position:absolute;left:0;width:1200px}
.abs{position:absolute}
.eyebrow{font-size:11px;font-weight:500;letter-spacing:.6px;color:var(--blue);text-transform:uppercase}
.section-title{font-size:30px;font-weight:600}
.center{text-align:center;left:0;width:1200px}
.btn{display:flex;align-items:center;justify-content:center;border-radius:20px;font-size:11px;font-weight:500}
.art{border-radius:24px}

/* Hero */
.hero{top:0;height:584px;background:linear-gradient(115deg,var(--hero-a) 0%,#3f84e2 45%,var(--hero-b) 100%);color:var(--white)}
.brand{display:flex;align-items:center;gap:10px}
.brand-dot{width:22px;height:22px;border-radius:50%;background:var(--white)}
.brand-name{font-size:24px;font-weight:500;color:var(--white)}
.nav{top:49px;left:473px;display:flex;gap:27px;font-size:11px;font-weight:500}
.nav a{color:var(--white);text-decoration:none}
.signup{top:40px;left:983px;width:105px;height:34px;background:var(--white);color:var(--blue)}
.hero h1{top:180px;left:112px;font-size:62px;line-height:70px;font-weight:700;color:var(--white)}
.hero-copy{top:342px;left:112px;width:420px;font-size:11.5px;line-height:19px;color:#eaf3ff}
.hero-cta{top:430px;left:112px;width:127px;height:35px;background:var(--white);color:var(--blue)}
.hero-art{top:128px;left:593px;width:458px;height:409px;background:linear-gradient(160deg,rgba(255,255,255,.28),rgba(40,70,200,.35))}

/* About */
.about{top:584px;height:531px}
.about-art{top:58px;left:168px;width:345px;height:425px;background:linear-gradient(160deg,#eaf1fc,#dde8fa)}
.about .eyebrow{top:84px;left:610px}
.about h2{top:112px;left:610px;font-size:29px;line-height:40px;font-weight:600;width:460px}
.about-copy{top:216px;left:610px;width:430px;font-size:11.5px;line-height:22.5px}
.about-cta{top:386px;left:610px;width:125px;height:37px;background:var(--blue);color:var(--white)}

/* Services */
.services{top:1115px;height:714px;background:var(--tint)}
.services .eyebrow{top:63px}
.services .section-title{top:94px}
.service-card{width:254px;height:219px;background:var(--white);box-shadow:var(--card-shadow);text-align:center;padding:20px 34px 0}
.service-card .icon{width:54px;height:54px;margin:0 auto 14px;border-radius:10px;background:linear-gradient(150deg,#cfe0fb,#5f8ef0)}
.service-card h3{font-size:14px;line-height:22px;font-weight:500;margin-bottom:10px;font-family:'Roboto',Arial,sans-serif}
.service-card p{font-size:10px;line-height:19px;color:var(--muted)}

/* Challenges */
.challenges{top:1829px;height:529px}
.challenges .eyebrow{top:72px;left:112px}
.challenges h2{top:100px;left:112px;font-size:28px;line-height:39px;font-weight:600}
.challenges-copy{top:193px;left:112px;width:532px;font-size:11px;line-height:22.4px}
.challenges-art{top:32px;left:690px;width:449px;height:497px;background:linear-gradient(160deg,#e9f0fc,#c8d9f7)}

/* Standard functionality */
.features{top:2358px;height:577px}
.features .eyebrow{top:42px}
.features .section-title{top:78px}
.feature-card{width:167px;height:162px;background:var(--white);box-shadow:var(--card-shadow);text-align:center;padding-top:28px}
.feature-card .icon{width:48px;height:48px;margin:0 auto 18px;border-radius:8px;background:linear-gradient(150deg,#ffd58a,#4d86ec)}
.feature-card h3{font-family:'Roboto',Arial,sans-serif;font-size:10.5px;line-height:14px;font-weight:700;padding:0 12px}

/* Testimonials */
.testimonials{top:2935px;height:433px;background:var(--tint)}
.testimonials .eyebrow{top:54px}
.testimonials .section-title{top:93px}
.quote-card{top:164px;width:438px;height:208px;background:var(--white);box-shadow:var(--card-shadow);padding:32px 36px}
.client{display:flex;gap:30px;align-items:flex-start}
.avatar{width:68px;height:68px;border-radius:50%;background:linear-gradient(150deg,#b9926f,#3c3a44)}
.client h3{font-family:'Roboto',Arial,sans-serif;font-size:14px;font-weight:700;margin-top:8px}
.client .role{font-size:9.5px;color:var(--muted);margin:7px 0 6px}
.stars{display:flex;gap:3px}
.quote{position:relative;margin-top:22px;padding:0 24px;font-size:9.5px;line-height:19px;color:var(--text)}
.quote::before,.quote::after{position:absolute;font-family:Georgia,serif;font-size:26px;color:#cfd3db}
.quote::before{content:"\201C";left:0;top:-8px}
.quote::after{content:"\201D";bottom:-22px;margin-left:6px}

/* Contact */
.contact{top:3368px;height:541px}
.contact-art{top:48px;left:128px;width:385px;height:434px;background:linear-gradient(160deg,#eaf1fc,#d2e1f8)}
.contact h2{top:65px;left:619px;font-size:29px;font-weight:600}
.field{left:621px;width:467px;height:50px;border:1px solid var(--line);background:var(--white);font-size:11px;color:var(--muted);padding:17px 16px}
.field.message{height:93px}
.submit{top:442px;left:621px;width:467px;height:48px;background:var(--blue);color:var(--white);font-size:13px;font-weight:700;display:flex;align-items:center;justify-content:center}

/* Footer */
.footer{top:3909px;height:223px;background:var(--blue-deep);color:var(--white)}
.footer .brand{top:54px;left:112px}
.socials{top:137px;left:112px;display:flex;gap:7px}
.socials span{width:25px;height:25px;border-radius:50%;border:1.5px solid var(--white)}
.copyright{top:182px;left:112px;font-size:9.5px}
.foot-col h4{font-size:10.5px;font-weight:700;margin-bottom:10px}
.foot-col li{list-style:none;font-size:10px;line-height:19px}
.newsletter h4{font-family:'Rubik',Arial,sans-serif;font-size:17px;font-weight:600;margin-bottom:12px}
.news-input{width:248px;height:36px;border:1px solid rgba(255,255,255,.85);font-size:9.5px;padding:12px 10px;color:#dce8ff}
.news-btn{width:248px;height:36px;background:var(--white);color:var(--blue);font-size:10.5px;font-weight:700;display:flex;align-items:center;justify-content:center;margin-top:12px}
</style>
</head>
<body>

<section class="hero">
  <div class="abs brand" style="top:46px;left:112px"><span class="brand-dot"></span><span class="brand-name">Ledgerly</span></div>
  <nav class="abs nav"><a>Home</a><a>About Us</a><a>Services</a><a>Standard Functionality</a><a>Testimonials</a><a>Contact</a></nav>
  <div class="abs btn signup">Sing Up</div>
  <h1 class="abs">Ledgerly<br>Made Simple</h1>
  <p class="abs hero-copy">Lorem ipsum dolor sit amet, consectetur adipiscing elit. Suspendisse feugiat tincidunt magna, ut faucibus erat iaculis eget. Etiam sed dolor elit. Aliquam non elementum tortor.</p>
  <div class="abs btn hero-cta">Get Started Now</div>
  <div class="abs art hero-art" role="img" aria-label="Vector illustration of two developers at a desk with code screen, cloud, gears and server racks"></div>
</section>

<section class="about">
  <div class="abs art about-art" role="img" aria-label="Vector illustration of a laptop with code, gears, clouds, documents and envelope"></div>
  <p class="abs eyebrow">About us</p>
  <h2 class="abs">Get Started With Our Software Agency</h2>
  <p class="abs about-copy">Ledgerly is a GDPR compliant Membership, Contact Management &amp; List Management solution Ideal replacement for any organisation or company still using Gridsheet, Mailroom, simple database or paper-based system to manage contact data, mail lists and other personalised information.Ledgerly offers a fast, secure, GDPR compliant solution for managing and coordinating all your Membership and Contact data, and generating GDPR compliant Marketing lists.</p>
  <div class="abs btn about-cta">Read More</div>
</section>

<section class="services">
  <p class="abs eyebrow center" style="text-align:center">Our services</p>
  <h2 class="abs section-title center">We Provide Ledgerly Services</h2>
  <div class="abs service-card" style="top:175px;left:184px"><div class="icon" role="img" aria-label="Consultancy icon"></div><h3>Consultancy</h3><p>Lorem ipsum dolor sit amet, consectetur adipiscing elit, sed do eiusmod tempor incididunt ut labore et dolore magna aliqua.</p></div>
  <div class="abs service-card" style="top:175px;left:474px"><div class="icon" role="img" aria-label="Data preparation icon"></div><h3>Data Preparation</h3><p>Lorem ipsum dolor sit amet, consectetur adipiscing elit, sed do eiusmod tempor incididunt ut labore et dolore magna aliqua.</p></div>
  <div class="abs service-card" style="top:175px;left:763px"><div class="icon" role="img" aria-label="Installation icon"></div><h3>Installation,Configuration<br>and Set-up of Main System</h3><p>Lorem ipsum dolor sit amet, consectetur adipiscing elit.</p></div>
  <div class="abs service-card" style="top:432px;left:184px"><div class="icon" role="img" aria-label="Training icon"></div><h3>Full Training</h3><p>Lorem ipsum dolor sit amet, consectetur adipiscing elit, sed do eiusmod tempor incididunt ut labore et dolore magna aliqua.</p></div>
  <div class="abs service-card" style="top:432px;left:474px"><div class="icon" role="img" aria-label="Technical support icon"></div><h3>Technical Support</h3><p>Lorem ipsum dolor sit amet, consectetur adipiscing elit, sed do eiusmod tempor incididunt ut labore et dolore magna aliqua.</p></div>
  <div class="abs service-card" style="top:432px;left:763px"><div class="icon" role="img" aria-label="Custom development icon"></div><h3>Optional Customised<br>Development Work</h3><p>Lorem ipsum dolor sit amet, consectetur adipiscing elit.</p></div>
</section>

<section class="challenges">
  <p class="abs eyebrow">Challenges</p>
  <h2 class="abs">Challenges Most<br>Organisations Encounter</h2>
  <p class="abs challenges-copy">One of the biggest challenges faced when moving from a manual record keeping system (Gridsheet, Mailroom, simple database, or paper etc.) is how to manage, and coordinate all the various silos of information, to arrive at a single, valid 'source of truth'.We can help you identify the sources of data you need to consider, and bring all your digital records together in a single de-duplicated list. This Master Data can be cleaned and categorised to show Opt-In preferences and areas of interest to assist with profiling/segmentation for future Mail lists. The Master Data will be returned for approval, and once agreed, will be imported for you with the necessary access permissions assigned; ready for you to start using the system from day one.Paper records, typically need to be entered manually, however, these records can also be organised to minimise duplication. We advise clients to enter this data themselves. This serves as a practical training exercise to familiarise your team with how the system works, and establish confidence. Operators working with manual systems quickly see how Ledgerly helps them establish a centralised source of truth, greatly reducing the time required to find information, and avoid the duplication – so often encountered with manual Gridsheet/Mailroom and paper-based processes.</p>
  <div class="abs art challenges-art" role="img" aria-label="Vector illustration of a man at a laptop in front of a task manager window with accept buttons"></div>
</section>

<section class="features">
  <p class="abs eyebrow center" style="text-align:center">Standard</p>
  <h2 class="abs section-title center">Standard Functionality</h2>
  <div class="abs feature-card" style="top:154px;left:112px"><div class="icon" role="img" aria-label="Attendance icon"></div><h3>Attendance Registration<br>&amp; Management</h3></div>
  <div class="abs feature-card" style="top:154px;left:314px"><div class="icon" role="img" aria-label="Time recording icon"></div><h3>Time Recording</h3></div>
  <div class="abs feature-card" style="top:154px;left:516px"><div class="icon" role="img" aria-label="Relationship icon"></div><h3>Relationship<br>Management</h3></div>
  <div class="abs feature-card" style="top:154px;left:718px"><div class="icon" role="img" aria-label="Tasks icon"></div><h3>Tasks/To-Do's</h3></div>
  <div class="abs feature-card" style="top:154px;left:921px"><div class="icon" role="img" aria-label="Notes icon"></div><h3>Notes/History</h3></div>
  <div class="abs feature-card" style="top:350px;left:112px"><div class="icon" role="img" aria-label="Document storage icon"></div><h3>Document storage</h3></div>
  <div class="abs feature-card" style="top:350px;left:314px"><div class="icon" role="img" aria-label="Donation icon"></div><h3>Donation Management</h3></div>
  <div class="abs feature-card" style="top:350px;left:516px"><div class="icon" role="img" aria-label="Prospect icon"></div><h3>Prospect Management</h3></div>
  <div class="abs feature-card" style="top:350px;left:718px"><div class="icon" role="img" aria-label="Secure access icon"></div><h3>Centralised, secure<br>permission-based access</h3></div>
  <div class="abs feature-card" style="top:350px;left:921px"><div class="icon" role="img" aria-label="GDPR storage icon"></div><h3>GDPR compliant storage<br>of all contact data</h3></div>
</section>

<section class="testimonials">
  <p class="abs eyebrow center" style="text-align:center">Testimonials</p>
  <h2 class="abs section-title center">What Our Clients Says</h2>
  <div class="abs quote-card" style="left:149px">
    <div class="client"><div class="avatar" role="img" aria-label="Client portrait"></div><div><h3>Tomas Reyner</h3><p class="role">Accountant , Fernbrook Ltd</p>
      <div class="stars"><svg width="86" height="15" viewBox="0 0 86 15"><g fill="#f7b500"><polygon id="s" points="7.5,0 9.4,5 14.5,5.4 10.5,8.7 11.8,14 7.5,11 3.2,14 4.5,8.7 0.5,5.4 5.6,5"/><use href="#s" x="18"/><use href="#s" x="36"/><use href="#s" x="54"/><use href="#s" x="72"/></g></svg></div></div></div>
    <p class="quote">What is the main benefit/output of the program for you? (Which functions make your work easier and why?</p>
  </div>
  <div class="abs quote-card" style="left:611px">
    <div class="client"><div class="avatar" role="img" aria-label="Client portrait"></div><div><h3>Iris Calloway</h3><p class="role">Public Relations , Fernbrook Ltd</p>
      <div class="stars"><svg width="86" height="15" viewBox="0 0 86 15"><g fill="#f7b500"><polygon id="t" points="7.5,0 9.4,5 14.5,5.4 10.5,8.7 11.8,14 7.5,11 3.2,14 4.5,8.7 0.5,5.4 5.6,5"/><use href="#t" x="18"/><use href="#t" x="36"/><use href="#t" x="54"/><use href="#t" x="72"/></g></svg></div></div></div>
    <p class="quote">Are there any other functions you would like to have? (What would these be and why?)Possibly online access to the data - Secure On-Line access is available when hosted on our cloud service</p>
  </div>
</section>

<section class="contact">
  <div class="abs art contact-art" role="img" aria-label="Vector illustration of a woman working at a desk with a monitor, chat bubble and plants"></div>
  <h2 class="abs">Contact Us</h2>
  <div class="abs field" style="top:110px">Your Name</div>
  <div class="abs field" style="top:182px">Your Email</div>
  <div class="abs field" style="top:254px">Your Phone</div>
  <div class="abs field message" style="top:326px">Message</div>
  <div class="abs submit">Submite</div>
</section>

<footer class="footer">
  <div class="abs brand"><span class="brand-dot"></span><span class="brand-name">Ledgerly</span></div>
  <div class="abs socials" aria-label="Social links"><span></span><span></span><span></span><span></span></div>
  <p class="abs copyright">© 2023 Ledgerly</p>
  <div class="abs foot-col" style="top:46px;left:308px"><h4>Important Links</h4><ul><li>Pricing</li><li>Resource Hub</li><li>Security</li><li>Privacy Policy</li><li>Terms of Use</li><li>Contact Us</li></ul></div>
  <div class="abs foot-col" style="top:46px;left:473px"><h4>Comparisons</h4><ul><li>Slotwise</li><li>Bookora</li><li>Teamhub</li><li>PlanPilot</li><li>Datewell</li><li>Pollmate</li><li>Helpnest</li></ul></div>
  <div class="abs foot-col" style="top:46px;left:637px"><h4>Company</h4><ul><li>Our story</li><li>Status</li><li>Terms of use</li><li>Privacy Policy</li><li>Sitemap</li></ul></div>
  <div class="abs newsletter" style="top:46px;left:789px"><h4>Subscribe To Our Newsletter</h4><div class="news-input">Enter your email</div><div class="news-btn">Subscribe Now</div></div>
</footer>

</body>
</html>
```